Flyer
Zielgruppe
Ich bin Energieberater für Wohngebäude. Ich möchte ein Flyer über meine Leistungen erstellen. Dabei möchte ich gezielt potentielle Partner wie Architekten und Immobilienverwalter ansprechen und ein Netzwerk aufbauen.
Meine Leistungen im Überblick:
- Energieberatung
- Individueller Sanierungsfahrplan (iSFP)
- Energieausweise
- TbH-Effizienzhaus-Planung (Neubau und Bestand)
- Planung klimafreundlicher Neubau (KFN)
- Fördermittelberatung und -beantragung
- PUL-Einzelmaßnahmen wie z. B. Dämmung der Gebäudehülle oder Fenstertausch uvm.
- Heizlastberechnung nach DIN EN 12831
- Hydraulischer Abgleich nach Verfahren A/B
- Heizflächenauslegung
- Wärmepumpen (Beratung und Auslegung)
Meine Signatur:
M. Eng. Torben Wiskow
Energieberater / Planungsingenieur
Volmar Haus
Lindholzgasse 7C
47263 Gelsenkirchen
Tel: 0152 / 871 43 06
E-Mail: info@Volmar-Haus.de
Aufgabenstellung
Ich möchte den Flyer sowohl als PDF-Format nutzen, um Kalt-Akquise übers Internet zu betreiben, als auch ausgedruckt.

```html
<!DOCTYPE html>
<html lang="de">
<head>
<meta charset="utf-8">
<title>Volmar Haus – Flyer</title>
<link rel="stylesheet" href="https://fonts.googleapis.com/css2?family=Merriweather:ital,wght@0,400;0,700;0,900;1,400&family=Lato:wght@400;700&display=swap">
<style>
  :root {
    --page-bg: #e6e7e9;
    --paper: #ffffff;
    --brand-blue: #168fd3;
    --brand-blue-deep: #0f7cc0;
    --navy: #0b3a66;
    --panel: #d6eaf8;
    --text-dark: #1f2a36;
    --logo-brown: #4a3832;
    --photo-light: #eceef0;
    --photo-mid: #c9ccd0;
  }
  * { box-sizing: border-box; margin: 0; padding: 0; }
  html, body { width: 1200px; height: 1117px; overflow: hidden; }
  body { background: var(--page-bg); position: relative; font-family: "Merriweather", Georgia, serif; }

  .flyer {
    position: absolute; left: 225px; top: 28px;
    width: 750px; height: 1060px;
    background: var(--paper);
    box-shadow: 0 10px 30px rgba(0,0,0,.18);
    overflow: hidden;
  }
  .flyer__shapes { position: absolute; inset: 0; }

  .headline {
    position: absolute; left: 30px; top: 438px; width: 690px;
    color: #fff; font-weight: 900; font-size: 41px; line-height: 1.15;
    text-align: center; letter-spacing: .2px;
  }

  .services {
    position: absolute; left: 262px; top: 548px; width: 460px;
  }
  .services__title {
    background: var(--brand-blue-deep); color: #fff;
    font-weight: 700; font-size: 18px;
    border-radius: 20px; padding: 9px 0; text-align: center;
  }
  .services__list {
    list-style: none; padding: 12px 18px 0 22px;
    font-size: 14.5px; line-height: 1.36; color: var(--text-dark);
  }
  .services__list li { position: relative; padding-left: 22px; }
  .services__list li::before {
    content: ""; position: absolute; left: 2px; top: 5px;
    width: 9px; height: 5px;
    border-left: 2.5px solid var(--brand-blue); border-bottom: 2.5px solid var(--brand-blue);
    transform: rotate(-45deg);
  }

  .brand { position: absolute; left: 0; top: 640px; width: 290px; text-align: center; }
  .brand__mark {
    width: 74px; height: 74px; border-radius: 50%;
    background: var(--brand-blue); margin: 0 auto 22px;
  }
  .brand__name {
    font-size: 25px; letter-spacing: 2.5px; color: var(--logo-brown); font-weight: 400;
  }
  .brand__tagline {
    font-family: "Lato", Arial, sans-serif; font-size: 13px; color: var(--logo-brown); margin-top: 4px;
  }

  .signature { position: absolute; left: 36px; top: 800px; width: 250px; }
  .signature__label { color: var(--brand-blue); font-size: 22px; font-weight: 400; }
  .signature__name { margin-top: 52px; font-size: 18px; font-weight: 700; color: var(--text-dark); }
  .signature__role { margin-top: 4px; font-size: 13px; font-style: italic; color: var(--text-dark); }

  .contact { position: absolute; left: 330px; top: 915px; color: #fff; }
  .contact__row { display: flex; align-items: flex-start; gap: 12px; margin-bottom: 6px; }
  .contact__icon { width: 20px; height: 20px; flex: none; margin-top: 4px; }
  .contact__company { font-size: 20px; font-weight: 700; }
  .contact__street { font-size: 15px; margin-top: 2px; }
  .contact__phone { font-size: 21px; font-weight: 700; }
  .contact__mail { font-size: 21px; font-weight: 700; }
</style>
</head>
<body>
<main class="flyer">
  <svg class="flyer__shapes" width="750" height="1060" viewBox="0 0 750 1060">
    <defs>
      <linearGradient id="photoTone" x1="0" y1="0" x2="1" y2="1">
        <stop offset="0" stop-color="var(--photo-light)"/>
        <stop offset=".55" stop-color="#dfe3e6"/>
        <stop offset=".8" stop-color="#e9d9a8"/>
        <stop offset="1" stop-color="var(--photo-mid)"/>
      </linearGradient>
      <linearGradient id="portraitTone" x1="0" y1="0" x2="0" y2="1">
        <stop offset="0" stop-color="#f1ece8"/>
        <stop offset="1" stop-color="#b79a86"/>
      </linearGradient>
    </defs>
    <rect class="hero-photo" x="0" y="0" width="750" height="470" fill="url(#photoTone)" role="img" aria-label="Foto: Bauplan mit Taschenrechner, Energieeffizienzskala und Hausmodell"/>
    <path class="band-blue" d="M0,380 L340,408 L350,378 L750,430 L750,1060 L0,1060 Z" fill="var(--brand-blue)"/>
    <path class="column-white" d="M0,560 Q160,548 292,612 L292,1000 L0,1000 Z" fill="var(--paper)"/>
    <path class="band-navy" d="M292,712 L750,650 L750,1060 L0,1060 L0,1002 L292,1002 Z" fill="var(--navy)"/>
    <circle cx="560" cy="330" r="112" fill="#d3d5d8"/>
    <circle cx="560" cy="330" r="104" fill="#ffffff"/>
    <circle class="portrait" cx="560" cy="330" r="96" fill="url(#portraitTone)" role="img" aria-label="Porträtfoto des Energieberaters"/>
    <rect class="services-panel" x="252" y="560" width="474" height="332" rx="24" fill="var(--panel)"/>
  </svg>

  <h1 class="headline">Ingenieurtechnische Planung<br>in der Energiewende!</h1>

  <section class="services">
    <h2 class="services__title">Meine Leistungen im Überblick:</h2>
    <ul class="services__list">
      <li>Energieberatung</li>
      <li>Individueller Sanierungsfahrplan (iSFP)</li>
      <li>Energieausweise</li>
      <li>TbH-Effizienzhaus-Planung (Neubau und Bestand)</li>
      <li>Planung klimafreundlicher Neubau (KFN)</li>
      <li>Fördermittelberatung und -beantragung</li>
      <li>PUL-Einzelmaßnahmen wie z. B. Dämmung der Gebäudehülle oder Fenstertausch uvm.</li>
      <li>Heizlastberechnung nach DIN EN 12831</li>
      <li>Hydraulischer Abgleich nach Verfahren A/B</li>
      <li>Heizflächenauslegung</li>
      <li>Wärmepumpen (Beratung und Auslegung)</li>
    </ul>
  </section>

  <div class="brand">
    <div class="brand__mark"></div>
    <div class="brand__name">VOLMAR HAUS</div>
    <div class="brand__tagline">Planung, Berechnung, Auslegung</div>
  </div>

  <div class="signature">
    <div class="signature__label">Meine Signatur:</div>
    <div class="signature__name">M. Eng. Torben Wiskow</div>
    <div class="signature__role">Energieberater / Planungsingenieur</div>
  </div>

  <address class="contact" style="font-style:normal">
    <div class="contact__row">
      <svg class="contact__icon" viewBox="0 0 20 20"><path d="M10 1a6.5 6.5 0 0 0-6.5 6.5C3.5 12.5 10 19 10 19s6.5-6.5 6.5-11.5A6.5 6.5 0 0 0 10 1z" fill="var(--brand-blue)"/><circle cx="10" cy="7.5" r="2.4" fill="var(--navy)"/></svg>
      <div><div class="contact__company">Volmar Haus</div><div class="contact__street">Lindholzgasse 7C</div></div>
    </div>
    <div class="contact__row">
      <svg class="contact__icon" viewBox="0 0 20 20"><circle cx="10" cy="10" r="10" fill="var(--brand-blue)"/><path d="M6.5 5.5l2 .2.8 2.2-1.2 1a6 6 0 0 0 2.8 2.8l1-1.2 2.2.8.2 2a1.5 1.5 0 0 1-1.6 1.2A8 8 0 0 1 5.3 7.1 1.5 1.5 0 0 1 6.5 5.5z" fill="var(--navy)"/></svg>
      <div class="contact__phone">0152 / 871 43 06</div>
    </div>
    <div class="contact__row">
      <svg class="contact__icon" viewBox="0 0 20 20"><circle cx="10" cy="10" r="10" fill="var(--brand-blue)"/><rect x="5" y="6.5" width="10" height="7" fill="none" stroke="var(--navy)" stroke-width="1.4"/><path d="M5 6.5l5 4 5-4" fill="none" stroke="var(--navy)" stroke-width="1.4"/></svg>
      <div class="contact__mail">info@Volmar-Haus.de</div>
    </div>
  </address>
</main>
</body>
</html>
```